Corvale Mechanical - Letterhead

We are a plumbing and hvac company based in Calgary. This letterhead will be on our quotes, invoices, preventative maintenance proposals etc.

```html
<!DOCTYPE html>
<html lang="en">
<head>
<meta charset="utf-8">
<title>Corvale Mechanical – Letterhead</title>
<link href="https://fonts.googleapis.com/css2?family=Open+Sans:wght@400;600;700;800&display=swap" rel="stylesheet">
<style>
  :root {
    --backdrop: #e4e4e5;
    --paper: #f6f6f7;
    --brand-blue: #2f6db5;
    --brand-orange: #e8562a;
    --body-grey: #6e6e70;
    --heading-grey: #3b3b3d;
    --ink-wash: #d9d9dc;
  }
  * { box-sizing: border-box; margin: 0; padding: 0; }
  html, body {
    width: 1200px; height: 945px; overflow: hidden;
    background: var(--backdrop);
    font-family: "Open Sans", Arial, sans-serif;
  }
  .letterhead {
    position: absolute; left: 257px; top: 18px;
    width: 686px; height: 909px;
    background: var(--paper);
    box-shadow: 0 2px 10px rgba(0,0,0,.12);
    overflow: hidden;
  }
  .brand {
    position: absolute; left: 56px; top: 58px;
    display: flex; align-items: center; gap: 10px;
  }
  .brand-dot {
    width: 30px; height: 30px; border-radius: 50%;
    background: var(--brand-orange);
  }
  .brand-name {
    font-weight: 800; font-size: 19px; line-height: 1.05;
    color: var(--brand-blue); letter-spacing: .5px; text-transform: uppercase;
  }
  .contact {
    position: absolute; right: 56px; top: 56px;
    text-align: right; font-size: 10.5px; line-height: 1.6; color: var(--body-grey);
  }
  .contact-row { display: flex; justify-content: flex-end; align-items: center; gap: 5px; }
  .contact-row svg { width: 9px; height: 9px; fill: var(--brand-orange); }
  .letter-body {
    position: absolute; left: 56px; top: 178px; width: 560px;
    color: var(--body-grey); font-size: 13.5px; line-height: 1.42;
  }
  .salutation {
    font-family: Arial, "Open Sans", sans-serif;
    font-weight: 700; font-size: 16px; color: var(--heading-grey);
    margin-bottom: 10px;
  }
  .letter-body p { margin-bottom: 18px; }
  .signature {
    position: absolute; left: 66px; top: 660px;
    width: 170px; height: 64px; border-radius: 6px;
    background: linear-gradient(90deg, var(--ink-wash), #ececee);
  }
  .footer { position: absolute; left: 0; bottom: 0; width: 686px; height: 70px; }
  .footer > svg { position: absolute; left: 0; top: 0; width: 686px; height: 70px; }
  .footer-address {
    position: absolute; left: 40px; bottom: 12px;
    display: flex; align-items: center; gap: 7px;
    color: #fff; font-size: 12px; line-height: 16px;
  }
  .footer-address svg { width: 11px; height: 14px; fill: #fff; }
  .footer-web {
    position: absolute; right: 62px; top: 14px;
    color: #fff; font-size: 12px; line-height: 16px; white-space: nowrap;
  }
  .footer-web strong { font-weight: 700; }
</style>
</head>
<body>
  <main class="letterhead">
    <header>
      <div class="brand">
        <span class="brand-dot"></span>
        <span class="brand-name">Corvale<br>Mechanical Inc</span>
      </div>
      <div class="contact">
        <div class="contact-row">855-555-0142
          <svg viewBox="0 0 10 10"><rect x="2" y="0" width="6" height="10" rx="1.2"/></svg>
        </div>
        <div class="contact-row">info@corvalemechanical.com
          <svg viewBox="0 0 10 10"><path d="M0 2h10v6H0z M0 2l5 3.5L10 2"/></svg>
        </div>
      </div>
    </header>

    <section class="letter-body">
      <h2 class="salutation">Dear Mr. Dorsey,</h2>
      <p>Lorem Ipsum is simply dummy text of the printing and typesetting industry. Lorem Ipsum has been the industry's standard dummy text ever since the 1500s, when an unknown printer took a galley of type and scrambled it to make a type specimen book. It has survived not only five centuries, but also the leap into electronic typesetting, remaining essentially unchanged.</p>
      <p>The standard chunk of Lorem Ipsum used since the 1500s is reproduced below for those interested. Sections 1.10.32 and 1.10.33 from "de Finibus Bonorum et Malorum" by Cicero are also reproduced in their exact original form, accompanied by English versions from the 1914 translation by H. Rackham</p>
      <p>Lorem Ipsum is simply dummy text of the printing and typesetting industry. Lorem Ipsum has been the industry's standard dummy text ever since the 1500s, when an unknown printer took a galley of type and scrambled it to make a type specimen book. It has survived not only five centuries, but also the leap into electronic typesetting, remaining essentially unchanged. It was popularised in the</p>
      <p>Lorem Ipsum is simply dummy text of the printing and typesetting industry. Lorem Ipsum has been the industry's standard dummy text ever since the 1500s, when an unknown printer took a galley of type and scrambled it to make a type specimen book. It has survived not only five centuries, but also the leap into electronic typesetting, remaining essentially unchanged. It was popularised in the</p>
    </section>

    <div class="signature" role="img" aria-label="Handwritten signature of the sender"></div>

    <footer class="footer">
      <svg viewBox="0 0 686 70" aria-hidden="true">
        <rect x="0" y="30" width="686" height="40" fill="var(--brand-blue)"/>
        <path d="M650 30 C664 22 668 8 672 0 L686 0 L686 30 Z" fill="var(--brand-blue)"/>
        <path d="M405 30 C418 14 430 8 455 8 L640 8 C652 8 656 4 659 0 L674 0 C668 16 660 38 630 40 L440 42 C422 42 412 38 405 30 Z" fill="var(--brand-orange)"/>
      </svg>
      <div class="footer-address">
        <svg viewBox="0 0 11 14"><path d="M5.5 0A5.5 5.5 0 0 0 0 5.5C0 9.5 5.5 14 5.5 14S11 9.5 11 5.5A5.5 5.5 0 0 0 5.5 0Zm0 7.6a2.1 2.1 0 1 1 0-4.2 2.1 2.1 0 0 1 0 4.2Z"/></svg>
        Po. Box 56, Street Name, City Name, Zip Code - 00000
      </div>
      <div class="footer-web">www.<strong>corvalemechanical</strong>.com</div>
    </footer>
  </main>
</body>
</html>
```